Creative & Professional Business Card for hair salon

We are looking to update our business cards. Our salon is creative, modern, progressive and professional and looking for a design that will reflect this.

```html
<!DOCTYPE html>
<html lang="en">
<head>
<meta charset="utf-8">
<title>Above the Mist – Business Card</title>
<link href="https://fonts.googleapis.com/css2?family=Lato:wght@300;400&family=Cormorant+Garamond:ital,wght@1,500&display=swap" rel="stylesheet">
<style>
  :root {
    --backdrop: #2b2b2b;
    --card: #ffffff;
    --brand-blue: #5f93b1;
    --ink-navy: #2d5a78;
    --ink-dark: #222222;
    --rule: #b9b9b9;
    --rule-light: #bcd3e2;
    --band: #4b7896;
    --icon-fill: #46708d;
  }
  * { margin: 0; padding: 0; box-sizing: border-box; }
  html, body { width: 1200px; height: 1200px; overflow: hidden; }
  body {
    background: var(--backdrop);
    position: relative;
    font-family: "Lato", sans-serif;
  }
  .card {
    position: absolute;
    top: 310px;
    width: 366px;
    height: 594px;
    background: var(--card);
    overflow: hidden;
  }
  .card--front { left: 233px; }
  .card--back { left: 628px; }

  .brand {
    position: absolute;
    left: 0; right: 0;
    display: flex;
    align-items: center;
    justify-content: center;
    gap: 12px;
    font-family: "Lato", sans-serif;
    font-weight: 300;
    font-size: 34px;
    color: var(--brand-blue);
    letter-spacing: 0.5px;
  }
  .brand__dot {
    width: 18px; height: 18px;
    border-radius: 50%;
    background: var(--brand-blue);
    flex: none;
  }
  .card--front .brand { top: 455px; top: 158px; }
  .card--back .brand { top: 130px; }

  .person {
    position: absolute;
    top: 316px; left: 0; right: 0;
    text-align: center;
  }
  .person__name {
    font-family: "Cormorant Garamond", serif;
    font-style: italic;
    font-weight: 500;
    font-size: 34px;
    line-height: 1;
    color: var(--ink-navy);
  }
  .person__role {
    margin-top: 6px;
    font-size: 17px;
    color: var(--ink-dark);
  }
  .contact-icons {
    position: absolute;
    top: 389px; left: 88px;
    width: 190px; height: 26px;
    display: flex; align-items: center; justify-content: center; gap: 2px;
  }
  .contact-icons::before, .contact-icons::after {
    content: ""; flex: 1; height: 1px; background: var(--rule); margin: 0 10px;
  }
  .contact-icons svg { width: 25px; height: 25px; }
  .contact-list {
    position: absolute;
    top: 426px; left: 0; right: 0;
    text-align: center;
    font-size: 17px;
    line-height: 22px;
    color: var(--ink-dark);
  }
  .contact-divider {
    position: absolute;
    top: 501px; left: 90px;
    width: 186px; height: 1px;
    background: var(--rule);
  }
  .address {
    position: absolute;
    top: 512px; left: 0; right: 0;
    text-align: center;
    font-size: 17px;
    line-height: 22px;
    color: var(--ink-dark);
  }

  .appointment__title {
    position: absolute;
    top: 250px; left: 0; right: 0;
    text-align: center;
    font-family: "Cormorant Garamond", serif;
    font-style: italic;
    font-weight: 500;
    font-size: 29px;
    color: var(--brand-blue);
  }
  .appointment__line {
    position: absolute;
    left: 40px; width: 287px; height: 1px;
    background: var(--rule-light);
  }
  .appointment__line--first { top: 344px; }
  .appointment__line--second { top: 415px; }

  .social-band {
    position: absolute;
    left: 0; right: 0; bottom: 0;
    height: 67px;
    background: var(--band);
  }
  .social-band__badge {
    position: absolute;
    top: 512px; left: 165px;
    width: 37px; height: 37px;
    border-radius: 50%;
    background: var(--band);
    border: 4px solid var(--card);
  }
  .social-band__url {
    position: absolute;
    top: 551px; left: 0; right: 0;
    text-align: center;
    font-size: 17px;
    color: #ffffff;
  }
</style>
</head>
<body>
  <section class="card card--front" aria-label="Business card front">
    <div class="brand"><span class="brand__dot"></span>Above the Mist</div>

    <div class="person">
      <p class="person__name">Daniel Hart</p>
      <p class="person__role">Managing Director</p>
    </div>

    <div class="contact-icons">
      <svg viewBox="0 0 26 26" aria-label="Phone">
        <circle cx="13" cy="13" r="12.5" fill="var(--icon-fill)"/>
        <path d="M7 11 q6 -5 12 0 l-1.5 2 h-2 l-0.5 -1.5 h-4 l-0.5 1.5 h-2z M8.5 14 h9 v4 h-9z" fill="#fff"/>
      </svg>
      <svg viewBox="0 0 26 26" aria-label="Email">
        <circle cx="13" cy="13" r="12.5" fill="var(--icon-fill)"/>
        <rect x="7" y="9" width="12" height="8.5" fill="#fff"/>
        <path d="M7 9 l6 5 l6 -5" stroke="var(--icon-fill)" stroke-width="1.2" fill="none"/>
      </svg>
      <svg viewBox="0 0 26 26" aria-label="Website">
        <circle cx="13" cy="13" r="12.5" fill="var(--icon-fill)"/>
        <circle cx="13" cy="13" r="6" fill="#fff"/>
        <path d="M10 10 q2 1 2 3 q-2 1 -1 4 M14 8 q1 2 3 2 q0 3 -2 5" stroke="var(--icon-fill)" stroke-width="1.3" fill="none"/>
      </svg>
    </div>

    <div class="contact-list">
      <p>044-987 654 321</p>
      <p>hello@mistsalon.com</p>
      <p>www.mistsalon.com</p>
    </div>
    <div class="contact-divider"></div>
    <div class="address">
      <p>87, Willow Lane Studio,</p>
      <p>30918 Eastmoor</p>
    </div>
  </section>

  <section class="card card--back" aria-label="Business card back">
    <div class="brand"><span class="brand__dot"></span>Above the Mist</div>

    <p class="appointment__title">Your Next Appointment</p>
    <div class="appointment__line appointment__line--first"></div>
    <div class="appointment__line appointment__line--second"></div>

    <div class="social-band"></div>
    <div class="social-band__badge"></div>
    <p class="social-band__url">www.mistsocial.com</p>
  </section>
</body>
</html>
```